Stationary

We have designed a new logo and business care.
It is now time for stationary.
We are a financial planning firm and are looking for something more formal that show the strength of our firm.
Please include our tag line; Integrity - Vision -Diligence.
I have uploaded a PDF of our current stationary - but - you are under no obligation to design anything like it.
Thx
Marta
Business

```html
<!DOCTYPE html>
<html lang="en">
<head>
<meta charset="utf-8">
<title>Harbor Crest Group – Stationery</title>
<link href="https://fonts.googleapis.com/css2?family=Source+Sans+3:wght@400;600&display=swap" rel="stylesheet">
<style>
  :root{
    --navy:#2b3990;
    --blue:#1b75bc;
    --paper:#f5f4f2;
    --ground:#a9a8a9;
    --ink:#4a4a4a;
    --body:#555;
  }
  *{margin:0;padding:0;box-sizing:border-box}
  html,body{width:1200px;height:796px;overflow:hidden;background:var(--ground);font-family:"Source Sans 3",sans-serif;color:var(--ink)}
  .sheet{position:absolute;background:var(--paper);box-shadow:0 1px 4px rgba(0,0,0,.25);overflow:hidden}
  .sheet svg.bands{position:absolute;inset:0;width:100%;height:100%}

  .letterhead{left:37px;top:33px;width:519px;height:729px}
  .brand{position:absolute;color:var(--navy);line-height:1}
  .brand .initials{display:flex;align-items:center;justify-content:center;gap:6px;font-size:24px;font-weight:400;letter-spacing:1px}
  .brand .initials::before{content:"";width:12px;height:12px;border-radius:50%;background:var(--navy)}
  .brand .name{font-size:13px;margin-top:7px;white-space:nowrap}
  .tagline{position:absolute;font-size:5.6px;letter-spacing:2.2px;color:var(--ink);font-weight:600;white-space:nowrap}
  .letterhead .brand{left:51px;top:50px;width:142px}
  .letterhead .tagline{left:51px;top:104px}
  .contact{position:absolute;right:48px;top:39px;text-align:right;font-size:10.4px;line-height:12.4px;color:var(--ink)}
  .contact .lines{margin-bottom:6px}
  .contact li{list-style:none;display:flex;justify-content:flex-end;align-items:center;gap:6px;line-height:13px}
  .contact svg{width:8px;height:8px;fill:var(--navy)}
  .letter{position:absolute;left:53px;top:231px;width:415px}
  .salutation{font-size:13.6px;margin-bottom:20px}
  .letter p{font-size:7.5px;line-height:12.4px;color:var(--body);text-align:justify;margin-bottom:12.4px}
  .closing{position:absolute;left:53px;top:510px;font-size:8px;color:var(--body)}
  .signature{position:absolute;left:52px;top:527px;width:66px;height:24px;background:#e6e5e3}
  .signer{position:absolute;left:55px;top:565px;font-size:8.8px;line-height:13px;color:var(--body)}
  .web{position:absolute;right:30px;bottom:8px;font-size:9px;letter-spacing:3.4px;color:#fff}

  .envelope-back{left:579px;top:210px;width:580px;height:264px}
  .envelope-back .mark{position:absolute;left:0;right:0;top:36px;text-align:center;color:#fff;font-size:28px;letter-spacing:1px;line-height:1}

  .envelope-front{left:578px;top:496px;width:582px;height:265px}
  .envelope-front .brand{left:26px;top:50px;width:142px}
  .envelope-front .tagline{left:26px;top:95px}
  .return{position:absolute;left:26px;top:108px;font-size:10.4px;line-height:12.4px;color:var(--ink)}
</style>
</head>
<body>

<section class="sheet letterhead">
  <svg class="bands" viewBox="0 0 519 729" preserveAspectRatio="none" aria-hidden="true">
    <path d="M0 0H519V3Q230 18 0 57Z" fill="var(--navy)"/>
    <path d="M0 729H519V673Q360 722 0 729Z" fill="var(--blue)"/>
    <path d="M0 729Q320 725 519 716V719Q330 727 0 729Z" fill="var(--navy)"/>
  </svg>

  <div class="brand"><div class="initials">HCG</div><div class="name">Harbor Crest Group</div></div>
  <div class="tagline">Prudence Clarity Commitment</div>

  <div class="contact">
    <div class="lines">2260 W. Alder Ave.<br>Riverton, WA 99150</div>
    <ul>
      <li>(555) 410-2887 <svg viewBox="0 0 10 10"><path d="M2 0l2 2-1 1.5q1 2 3 3L7.5 5.5l2 2L8 9.5Q4 10 .5 2z"/></svg></li>
      <li>(555) 410-2889 <svg viewBox="0 0 10 10"><path d="M2 0h6v3H2zM0 4h10v4H8v2H2V8H0z"/></svg></li>
      <li>name@hcg.com <svg viewBox="0 0 10 10"><path d="M0 2h10v6H0zM1 3l4 3 4-3" stroke="#f5f4f2" stroke-width=".8"/></svg></li>
    </ul>
  </div>

  <article class="letter">
    <div class="salutation">Dear Mr. Reyes,</div>
    <p>Lorem ipsum dolor sit amet, consectetur adipiscing elit. Donec orci purus, luctus vitae dignissim eu, iaculis sed purus. Vivamus faucibus, ipsum nec aliquet viverra, leo mauris condimentum ligula, sit amet sagittis enim ligula quis arcu. Nam egestas tortor id nisi porttitor mattis. In tortor ante, ultricies in suscipit a, tempus non massa. Vivamus et auctor mi. Fusce vel massa nulla. Phasellus nec eros mauris, et scelerisque orci.</p>
    <p>Donec malesuada orci vitae nulla accumsan porta a id massa. Quisque accumsan iaculis magna sit amet fringilla. Maecenas consequat, magna eget tincidunt semper, odio nibh rutrum mi, id feugiat ante nisi eu risus. Vestibulum nunc orci, rhoncus a placerat in, ultricies in mi. Cras mattis varius eros, vel fringilla nisi suscipit eget. Quisque scelerisque sagittis nulla at porttitor.</p>
    <p>Sed id augue vitae urna euismod commodo aliquet a quam. Pellentesque arcu velit, cursus et malesuada ut, consequat et diam. Nullam erat sem, rhoncus id ullamcorper vitae, rhoncus et arcu. In ultricies ultricies nulla, ut rutrum nisi iaculis at. Donec eu magna a metus ornare faucibus. Fusce aliquet faucibus ultricies. Morbi semper, est id tincidunt gravida, sem arcu adipiscing lacus, ac bibendum nulla leo eu purus. Quisque nec diam sed risus consectetur accumsan quis quis nibh. Vestibulum id purus lorem.</p>
    <p>It is a long established fact that a reader will be distracted by the readable content of a page when looking at its layout. The point of using Lorem Ipsum is that it has a more-or-less normal distribution of letters, as opposed to using 'Content here, content here', making it look like readable English. Many desktop publishing packages</p>
  </article>

  <div class="closing">Sincerely,</div>
  <div class="signature" role="img" aria-label="Handwritten signature"></div>
  <div class="signer">Daniel Reyes<br>CEO/ Founder</div>

  <div class="web">www.hcg.com</div>
</section>

<section class="sheet envelope-back">
  <svg class="bands" viewBox="0 0 580 264" preserveAspectRatio="none" aria-hidden="true">
    <path d="M0 0H580L568 70Q565 96 540 96H45Q22 96 15 75Z" fill="var(--navy)"/>
  </svg>
  <div class="mark">HCG</div>
</section>

<section class="sheet envelope-front">
  <svg class="bands" viewBox="0 0 582 265" preserveAspectRatio="none" aria-hidden="true">
    <path d="M0 0H582V2Q250 14 0 58Z" fill="var(--navy)"/>
    <path d="M0 265H582V207Q420 250 0 265Z" fill="var(--blue)"/>
  </svg>
  <div class="brand"><div class="initials">HCG</div><div class="name">Harbor Crest Group</div></div>
  <div class="tagline">Prudence Clarity Commitment</div>
  <div class="return">2260 W. Alder Ave.,<br>Riverton, WA 99150</div>
</section>

</body>
</html>
```